Tolvek Acres brand , chocolate packaging design

Tolvek Acres

Products List

CANNABIS INFUSED CHOCOLATE BAR
(4 Flavor Chocolate Bar)
Original Milk chocolate Bar
Cookies N Cream Bar
Strawberry Cheesecake Bar
S’mores Bar

Information Front
-1000 MG THC Per package
-100mg THC per serving
-Made with Belgian Chocolate
-Made with Quality California Cannabis Extracts
-Net weight of bar 50grams
-California triangle warning symbol
-Flavor of chocolate bar

Information Back

-10 Servings per package
-100 mg serving size

-Directions
Wait 1-2 hours for full effect before consuming more.
-Very potent , Keep out of reach of children

-Store at 68-77° F
-Will melt in prolonged heat
-California government warning and p65warning website

Ingredient list

Milk chocolate Bar
MILK CHOCOLATE (SUGAR, COCOA BUTTER , UNSWEETENED CHOCOLATE, SUNFLOWER LECITHIN, VANILLA) , CANNABIS EXTRACT.
ALLERGENS-CONTAINS MILK

Strawberry Cheesecake
WHITE CHOCOLATE (SUGAR, COCOA BUTTER, WHOLE MILK POWDER ,SOY LECITHIN, NATURAL VANILLA FLAVOR) STRAWBERRY POWDER , STRAWBERRY EXTRACT , NATURAL FLAVORS, CANNABIS EXTRACT.

Cookies n cream
WHITE CHOCOLATE (SUGAR, COCOA BUTTER, WHOLE MILK POWDER ,SOY LECITHIN, NATURAL VANILLA FLAVOR) 9
BRANZIES (SUGAR, WHITE RICE FLOUR, TAPIOCA STARCH, PALM OIL, CANOLA OIL, WHOLE OAT FLOUR, CORN STARCH , COCOA (PROCESSED WITH ALKALI), INVERT SUGAR, SOY LECITHIN, BAKING SODA, SALT, XANTHAM GUM , CHOCOLATE, ARTIFICIAL FLAVOR, CANNABIS EXTRACT

S’mores
MILK CHOCOLATE (SUGAR, COCOA BUTTER, MILK, UNSWEETENED CHOCOLATE ,SUNFLOWER LECITHIN, VANILLA), MARSHMALLOW (SUGAR ,CORN SYRUP , MODIFIED STARCH, GELATIN, SODIUM HEXAMETAPHOSPHATE, ARTIFICIAL FLAVOR , NATURAL FLAVOR , ARTIFICIAL COLO (BLUE 1)), GRAHAM CRACKER (CORN STARCH, BROWN SUGAR , CORN FLOUR, PALM FAT , SOY FLOUR , SOY BRAN, HONEY, MODIFIED TAPIOCA STARCH, AMMONIUM BICARBONATE, BAKING SODA, SALT, CARAMELIZED SUGAR) NATURAL FLAVOR, CANNABIS EXTRACT.

Looking for simple clean modern design , chocolate bar can be like miravelle of like the Quendrith one with images on it , and gummy is a mylar bag I really like the Quendrith style , I can provide dieline etc thank you !

Target Market(s)

Young adults

Industry/Entity Type

Cannabis , Delta 8 , CBD

Requirements
Must have
• Chocolate bar is box , dielines Included with images
Nice to have
• Simple clean , elegant and modern design , like the miravelle and Quendrith brands , white logo preferred

```html
<!DOCTYPE html>
<html lang="en">
<head>
<meta charset="utf-8">
<title>Tolvek Acres – Chocolate Bar Packaging</title>
<link rel="stylesheet" href="https://fonts.googleapis.com/css2?family=Bebas+Neue&family=Oswald:wght@300;400&family=Mrs+Saint+Delafield&display=swap">
<style>
  :root {
    --charcoal: #373737;
    --white: #ffffff;
    --smores: #efdccb;
    --smores-script: #d9a388;
    --milk: #75483c;
    --cookies: #d9a388;
    --strawberry: #a84439;
    --dot: #efdccb;
  }
  * { margin: 0; padding: 0; box-sizing: border-box; }
  html, body {
    width: 1200px; height: 749px; overflow: hidden;
    background: var(--white);
  }
  .lineup { position: relative; width: 1200px; height: 749px; }
  .pack {
    position: absolute; top: 93px; width: 245px; height: 574px;
    --accent: var(--milk); --label-ink: var(--white); --script: var(--milk);
  }
  .pack--smores { left: 49px; --accent: var(--smores); --label-ink: var(--charcoal); --script: var(--smores-script); }
  .pack--milk { left: 328px; --accent: var(--milk); --script: var(--milk); }
  .pack--cookies { left: 613px; --accent: var(--cookies); --script: var(--cookies); }
  .pack--strawberry { left: 891px; --accent: var(--strawberry); --script: var(--strawberry); }

  .front {
    position: absolute; left: 0; top: 0; width: 245px; height: 416px;
    background: var(--charcoal); color: var(--white); text-align: center;
  }
  .front__tab {
    position: absolute; left: 114px; top: 0; width: 25px; height: 32px;
    background: var(--accent);
  }
  .brand {
    position: absolute; left: 0; right: 0; top: 144px;
    font-family: "Bebas Neue", sans-serif; font-size: 38px; line-height: 1;
    letter-spacing: 3px;
  }
  .product {
    position: absolute; left: 0; right: 0; top: 259px;
    font-family: "Bebas Neue", sans-serif; font-size: 24px; line-height: 28px;
    letter-spacing: 3px;
  }
  .dots {
    position: absolute; left: 0; right: 0; top: 341px;
    display: flex; justify-content: center; gap: 5px;
  }
  .dots span { width: 3px; height: 3px; border-radius: 50%; background: var(--dot); }
  .dose {
    position: absolute; left: 0; right: 0; top: 365px;
    font-family: "Bebas Neue", sans-serif; font-size: 17px; line-height: 1;
    letter-spacing: 0.5px;
  }
  .dose__unit {
    position: absolute; left: 0; right: 0; top: 386px;
    font-family: "Oswald", sans-serif; font-weight: 300; font-size: 8px;
    letter-spacing: 1.3px;
  }
  .flavor {
    position: absolute; left: 0; right: 0; top: 418px;
    font-family: "Mrs Saint Delafield", cursive; font-size: 30px; line-height: 38px;
    text-align: center; color: var(--script);
  }
  .label {
    position: absolute; left: 0; top: 455px; width: 245px; height: 119px;
    background: var(--accent); color: var(--label-ink);
    font-family: "Oswald", sans-serif; font-weight: 400; text-align: center;
  }
  .label__claim {
    position: absolute; left: 0; right: 0; top: 15px;
    font-size: 8.5px; letter-spacing: 1.2px;
  }
  .label__rule {
    position: absolute; left: 74px; top: 38px; width: 106px; height: 1.5px;
    background: var(--label-ink);
  }
  .label__origin {
    position: absolute; left: 60px; right: 0; top: 53px;
    font-size: 8.5px; letter-spacing: 1.2px; text-align: left;
  }
  .warning {
    position: absolute; left: 10px; top: 55px; width: 44px; height: 50px;
  }
  .net-weight {
    position: absolute; left: 68px; top: 83px; width: 122px; height: 18px;
    background: var(--charcoal); color: var(--white);
    font-size: 10px; line-height: 18px; letter-spacing: 1.3px; font-weight: 300;
  }
</style>
</head>
<body>
<main class="lineup">

  <section class="pack pack--smores">
    <div class="front">
      <div class="front__tab"></div>
      <h1 class="brand">TOLVEK ACRES</h1>
      <p class="product">CANNABIS INFUSED<br>CHOCOLATE BAR</p>
      <div class="dots"><span></span><span></span><span></span></div>
      <p class="dose">1000 MG THC | 100MG THC</p>
      <p class="dose__unit">PER PACKAGE &nbsp;| PER SERVING</p>
    </div>
    <p class="flavor">S’mores</p>
    <div class="label">
      <p class="label__claim">WITH QUALITY CALIFORNIA CANNABIS EXTRACTS</p>
      <div class="label__rule"></div>
      <p class="label__origin">MADE WITH BELGIAN CHOCOLATE</p>
      <svg class="warning" viewBox="0 0 44 50" aria-hidden="true"><path d="M22 4 L41 38 L3 38 Z" fill="none" stroke="var(--label-ink)" stroke-width="3.5" stroke-linejoin="round"/></svg>
      <p class="net-weight">NET WEIGHT: 50GRAMS</p>
    </div>
  </section>

  <section class="pack pack--milk">
    <div class="front">
      <div class="front__tab"></div>
      <h1 class="brand">TOLVEK ACRES</h1>
      <p class="product">CANNABIS INFUSED<br>CHOCOLATE BAR</p>
      <div class="dots"><span></span><span></span><span></span></div>
      <p class="dose">1000 MG THC | 100MG THC</p>
      <p class="dose__unit">PER PACKAGE &nbsp;| PER SERVING</p>
    </div>
    <p class="flavor">Original Milk</p>
    <div class="label">
      <p class="label__claim">WITH QUALITY CALIFORNIA CANNABIS EXTRACTS</p>
      <div class="label__rule"></div>
      <p class="label__origin">MADE WITH BELGIAN CHOCOLATE</p>
      <svg class="warning" viewBox="0 0 44 50" aria-hidden="true"><path d="M22 4 L41 38 L3 38 Z" fill="none" stroke="var(--label-ink)" stroke-width="3.5" stroke-linejoin="round"/></svg>
      <p class="net-weight">NET WEIGHT: 50GRAMS</p>
    </div>
  </section>

  <section class="pack pack--cookies">
    <div class="front">
      <div class="front__tab"></div>
      <h1 class="brand">TOLVEK ACRES</h1>
      <p class="product">CANNABIS INFUSED<br>CHOCOLATE BAR</p>
      <div class="dots"><span></span><span></span><span></span></div>
      <p class="dose">1000 MG THC | 100MG THC</p>
      <p class="dose__unit">PER PACKAGE &nbsp;| PER SERVING</p>
    </div>
    <p class="flavor">Cookies N Cream</p>
    <div class="label">
      <p class="label__claim">WITH QUALITY CALIFORNIA CANNABIS EXTRACTS</p>
      <div class="label__rule"></div>
      <p class="label__origin">MADE WITH BELGIAN CHOCOLATE</p>
      <svg class="warning" viewBox="0 0 44 50" aria-hidden="true"><path d="M22 4 L41 38 L3 38 Z" fill="none" stroke="var(--label-ink)" stroke-width="3.5" stroke-linejoin="round"/></svg>
      <p class="net-weight">NET WEIGHT: 50GRAMS</p>
    </div>
  </section>

  <section class="pack pack--strawberry">
    <div class="front">
      <div class="front__tab"></div>
      <h1 class="brand">TOLVEK ACRES</h1>
      <p class="product">CANNABIS INFUSED<br>CHOCOLATE BAR</p>
      <div class="dots"><span></span><span></span><span></span></div>
      <p class="dose">1000 MG THC | 100MG THC</p>
      <p class="dose__unit">PER PACKAGE &nbsp;| PER SERVING</p>
    </div>
    <p class="flavor">Strawberry Cheesecake</p>
    <div class="label">
      <p class="label__claim">WITH QUALITY CALIFORNIA CANNABIS EXTRACTS</p>
      <div class="label__rule"></div>
      <p class="label__origin">MADE WITH BELGIAN CHOCOLATE</p>
      <svg class="warning" viewBox="0 0 44 50" aria-hidden="true"><path d="M22 4 L41 38 L3 38 Z" fill="none" stroke="var(--label-ink)" stroke-width="3.5" stroke-linejoin="round"/></svg>
      <p class="net-weight">NET WEIGHT: 50GRAMS</p>
    </div>
  </section>

</main>
</body>
</html>
```